New emergency medical service needs a marketing flyer for prospective customers

We need a tri fold brochure on an 8.5 X 11 stock for a new emergency medical service in Pennsylvania. We provide basic first aid and now Covid-19 pre screening and temperature monitoring for special events, large gatherings and businesses. Examples of these would be but not limited to: Sporting events, carnivals, festivals, craft shows, warehouses, churches, manufacturing facilities, industrial buildings, large construction sites, multi occupancy officer buildings. The market for this is pretty much untouched and endless. we would like to use gray as the back ground color and obviously our logo. The final design should grab their attention and communicate the importance of having trained and certified professionals at their event or facility. We want to give them that piece of mind they are in good hands with us.

Target Market(s)

primary focus is going to be on businesses with large offices, large buildings or lots of foot traffic in and out of the building

Requirements
Must have
• gray background, pictures, company phone # , company web site, and contact email address. I will provide all that information to the winner to add at the end.
Nice to have
• pictures that covers the whole front cover with logo at top

```html
<!DOCTYPE html>
<html lang="en">
<head>
<meta charset="utf-8">
<title>KVR Medical Services – Tri-fold Brochure</title>
<link rel="stylesheet" href="https://fonts.googleapis.com/css2?family=Arimo:wght@400;700&family=Roboto+Condensed:wght@700&display=swap">
<style>
:root{
  --stage:#d6d6d6;
  --sheet-gray:#5e5d62;
  --panel-gray:#67666b;
  --teal-dark:#2e4353;
  --teal-deep:#1d2d38;
  --charcoal:#2c2c2e;
  --charcoal-2:#323234;
  --bar:#6e6d72;
  --white:#ffffff;
  --soft:#e4e4e6;
  --muted:#9a9aa0;
  --brand-blue:#1418b8;
  --brand-teal:#1aa39a;
  --circle:#3a3a40;
}
*{box-sizing:border-box;margin:0;padding:0}
html,body{width:797px;height:1200px;overflow:hidden;background:var(--stage)}
body{position:relative;font-family:"Arimo",Arial,sans-serif;color:var(--white)}
.sheet{position:absolute;left:35px;width:726px;height:562px;overflow:hidden}
.sheet--outside{top:28px;background:var(--sheet-gray)}
.sheet--inside{top:615px;background:var(--charcoal)}
.abs{position:absolute}
.photo{position:absolute}
p{font-size:8.4px;line-height:11px;text-align:justify}
h2{font-weight:700}

/* outside */
.about-photo{left:0;top:0;width:248px;height:189px;background:linear-gradient(135deg,#566f80,#3b5566 55%,#2d4351)}
.about-panel{left:0;top:189px;width:248px;height:373px;background:var(--teal-dark);opacity:.96}
.cover-photo{left:248px;top:0;width:478px;height:562px;background:linear-gradient(160deg,#6a696e,#56555a 45%,#6f6e73 80%,#5d5c61)}
.fold{position:absolute;top:0;width:1px;height:100%;background:rgba(255,255,255,.08)}
.about-title{left:0;width:248px;top:200px;text-align:center;font-size:12.5px}
.about-text-1{left:18px;top:231px;width:207px}
.about-text-2{left:21px;top:371px;width:204px}
.services-title{left:248px;width:235px;top:21px;text-align:center;font-size:19px;line-height:24px}
.services-lead{left:250px;width:230px;top:91px;text-align:center;font-size:11px;line-height:14.5px;font-weight:700;letter-spacing:-.3px}
.services-list{left:274px;top:136px;list-style:none}
.services-list li{height:16.5px;font-size:8.7px;display:flex;align-items:center;color:var(--soft)}
.services-list b{width:15px;font-size:10.5px;color:var(--white)}
.brand{display:flex;align-items:center;gap:6px}
.brand-mark{width:22px;height:22px;border-radius:50%;flex:none}
.brand-name{font-family:"Arimo",Arial,sans-serif;font-weight:700;line-height:1}
.brand-name span{display:block;font-size:10px;letter-spacing:1px;margin-top:3px}
.brand--mid{left:275px;top:306px;color:#c9c9cc}
.brand--mid .brand-mark{background:#c9c9cc}
.brand--mid .brand-name{font-size:34px}
.brand--cover{left:509px;top:34px;color:var(--brand-blue)}
.brand--cover .brand-mark{background:var(--brand-blue)}
.brand--cover .brand-name{font-size:42px}
.contact-title{left:248px;width:256px;top:385px;text-align:center;font-size:12.5px}
.contact-block{left:271px;top:416px;font-size:8.6px;line-height:11px;font-weight:700}
.web{font-size:8.8px;font-weight:700;text-align:center}
.web--mid{left:283px;width:131px;top:528px}
.web--cover{left:521px;width:165px;top:528px}
.cover-circle{left:576px;top:108px;width:108px;height:108px;border-radius:50%;background:var(--circle);opacity:.85}
.cover-tagline{left:492px;width:226px;top:468px;text-align:center;font-size:10.6px;line-height:13.5px;color:var(--soft)}

/* inside */
.swab-photo{left:0;top:0;width:486px;height:266px;background:linear-gradient(120deg,#5c5c5e,#3e3e40 50%,#2a2a2b)}
.inside-left{left:0;top:266px;width:245px;height:296px;background:var(--charcoal)}
.inside-mid{left:245px;top:266px;width:241px;height:296px;background:var(--charcoal-2)}
.inside-right{left:486px;top:0;width:240px;height:562px;background:linear-gradient(180deg,#111a20,var(--teal-deep) 30%,#26394a)}
.bottom-bar{left:0;top:538px;width:452px;height:13px;background:var(--bar)}
.h-lorem{font-family:"Roboto Condensed","Arial Narrow",sans-serif;font-size:15.5px;line-height:19px;letter-spacing:.3px}
.h-lorem--left{left:24px;top:277px}
.h-lorem--mid{left:300px;width:152px;top:234px;text-align:right}
.inside-text-1{left:24px;top:322px;width:198px}
.inside-text-2{left:24px;top:442px;width:198px}
.web--inside{left:0;width:216px;top:524px}
.step{position:absolute;left:260px;width:192px;display:flex}
.step b{width:38px;font-size:30px;line-height:28px;color:#8f8f94;font-family:"Arimo",Arial,sans-serif}
.step p{width:154px;color:var(--soft)}
.covid-title{left:486px;width:240px;top:22px;text-align:center;font-size:40px;line-height:44px}
.covid-sub{left:486px;width:240px;top:69px;text-align:center;font-size:17px}
.covid-lead{left:496px;width:222px;top:120px;text-align:center;font-size:11.2px;line-height:14.5px;font-weight:700}
.covid-text{left:494px;top:198px;width:212px;color:var(--soft)}
.brand--back{left:508px;top:478px;color:#b6b8bf}
.brand--back .brand-mark{background:#b6b8bf}
.brand--back .brand-name{font-size:38px}
</style>
</head>
<body>

<section class="sheet sheet--outside" aria-label="Brochure outside spread">
  <div class="photo cover-photo" role="img" aria-label="Photo of office staff in masks having temperature checked by a medic in protective suit"></div>
  <div class="photo about-photo" role="img" aria-label="Photo of two masked business colleagues talking in an office"></div>
  <div class="abs about-panel"></div>
  <span class="fold" style="left:248px"></span>
  <span class="fold" style="left:486px"></span>

  <h2 class="abs about-title">ABOUT US</h2>
  <p class="abs about-text-1">Lorem ipsum dolor sit amet, consectetuer adipiscing elit, sed diam nonummy nibh euismod tincidunt ut laoreet dolore magna aliquam erat volutpat. Ut wisi enim ad minim veniam, quis nostrud exerci tation ullamcorper suscipit lobortis nisl ut aliquip ex ea commodo consequat. Duis autem vel eum iriure dolor in hendrerit in vulputate velit esse molestie consequat, vel illum dolore eu feugiat nulla facilisis at vero eros et accumsan et iusto odio dignissim qui blandit praesent luptatum zzril delenit augue duis dolore te feugait nulla facilisi.</p>
  <p class="abs about-text-2">Lorem ipsum dolor sit amet, consectetuer adipiscing elit, sed diam nonummy nibh euismod tincidunt ut laoreet dolore magna aliquam erat volutpat. Ut wisi enim ad minim veniam, quis nostrud exerci tation ullamcorper suscipit lobortis nisl ut aliquip ex ea commodo consequat. Duis autem vel eum iriure dolor in hendrerit in vulputate velit esse molestie consequat, vel illum dolore eu feugiat nulla facilisis at vero eros et accumsan et iusto odio dignissim qui blandit praesent luptatum zzril delenit augue duis dolore te feugait nulla facilisi.<br>Lorem ipsum dolor sit amet, cons</p>

  <h2 class="abs services-title">SERVICES<br>WE OFFER</h2>
  <div class="abs services-lead">Lorem ipsum dolor sit amet, consectetuer adipiscing elit, sed diam nonummy nibh</div>
  <ol class="abs services-list">
    <li><b>1</b>Diam nonummy nibh euismod</li>
    <li><b>2</b>tincidunt ut laoreet dolore magna</li>
    <li><b>3</b>aliquam erat volutpat. Ut wisi enim</li>
    <li><b>4</b>ad minim veniam, quis nostrud exerci</li>
    <li><b>5</b>tation ullamcorper suscipit lobortis nisl ut</li>
    <li><b>6</b>aliquip ex ea commodo consequat.</li>
  </ol>

  <div class="abs brand brand--mid"><span class="brand-mark"></span><div class="brand-name">KVR<span>Medical Services</span></div></div>

  <h2 class="abs contact-title">CONTACT US</h2>
  <address class="abs contact-block" style="font-style:normal">
    Delfon 18 Str.<br>15344, Pallini<br>Athens,<br>Greece<br><br>
    +30-2100000147 (landline)<br>+30-6900000258 (mobile phone)<br>+30-2100000369 (fax)
  </address>
  <div class="abs web web--mid">www,website.com</div>

  <div class="abs brand brand--cover"><span class="brand-mark"></span><div class="brand-name">KVR<span>Medical Services</span></div></div>
  <div class="abs cover-circle"></div>
  <div class="abs cover-tagline">Provide certified medical professionals for<br>medical standbys at events and businesses.</div>
  <div class="abs web web--cover">www,website.com</div>
</section>

<section class="sheet sheet--inside" aria-label="Brochure inside spread">
  <div class="photo swab-photo" role="img" aria-label="Photo of a medic in mask and face shield taking a swab test"></div>
  <div class="abs inside-left"></div>
  <div class="abs inside-mid"></div>
  <div class="abs inside-right"></div>
  <div class="abs bottom-bar"></div>

  <h2 class="abs h-lorem h-lorem--left">LOREM IPSUM<br>DOLOR AGNA</h2>
  <p class="abs inside-text-1">Lorem ipsum dolor sit amet, consectetuer adipiscing elit, sed diam nonummy nibh euismod tincidunt ut laoreet dolore magna aliquam erat volutpat. Ut wisi enim ad minim veniam, quis nostrud exerci tation ullamcorper suscipit lobortis nisl ut aliquip ex ea commodo consequat. Duis autem vel eum iriure dolor in hendrerit in vulputate velit esse molestie consequat, vel illum dolore eu feugiat nulla facilisis at vero eros et accumsan</p>
  <p class="abs inside-text-2">Lorem ipsum dolor sit amet, consectetuer adipiscing elit, sed diam nonummy nibh euismod tincidunt ut laoreet dolore magna aliquam erat volutpat. Ut wisi enim ad minim veniam, quis nostrud exerci tation ullamcorper suscipit lobortis nisl ut aliquip ex ea commodo consequat.</p>
  <div class="abs web web--inside">www,website.com</div>

  <h2 class="abs h-lorem h-lorem--mid">LOREM IPSUM<br>DOLOR AGNA</h2>
  <div class="step" style="top:275px"><b>1</b><p>Sed ut perspiciatis unde omnis iste natus error sit voluptatem accusantium doloremque laudantium, totam rem aperiam, eaque ipsa quae ab illo inventore veritatis et quasi architecto beatae vitae dicta sunt explicabo.</p></div>
  <div class="step" style="top:352px"><b>2</b><p>Nemo enim ipsam voluptatem quia voluptas sit aspernatur aut odit aut fugit, sed quia consequuntur magni dolores eos qui ratione voluptatem sequi nesciunt.</p></div>
  <div class="step" style="top:418px"><b>3</b><p>Neque porro quisquam est, qui dolorem ipsum quia dolor sit amet, consectetur, adipisci velit, sed quia non numquam eius modi tempora incidunt ut labore et dolore magnam aliquam quaerat voluptatem.</p></div>
  <div class="step" style="top:496px"><b>4</b><p>Ut enim ad minima veniam, quis nostrum exercitationem ullam corporis suscipit laboriosam, nisi ut aliquid ex ea</p></div>

  <h1 class="abs covid-title">COVID-19</h1>
  <h2 class="abs covid-sub">Providing First Aid Care</h2>
  <div class="abs covid-lead">Learn how to prepare your health-care facility for a hurricane or other natural disaster during COVID-19.</div>
  <p class="abs covid-text">Lorem ipsum dolor sit amet, consectetuer adipiscing elit, sed diam nonummy nibh euismod tincidunt ut laoreet dolore magna aliquam erat volutpat. Ut wisi enim ad minim veniam, quis nostrud exerci tation ullamcorper suscipit lobortis nisl ut aliquip ex ea commodo consequat. Duis autem vel eum iriure dolor in hendrerit in vulputate velit esse molestie consequat, vel illum dolore eu feugiat nulla facilisis at vero eros et accumsan et iusto odio dignissim qui blandit praesent luptatum zzril delenit augue duis dolore te feugait nulla facilisi.<br>Lorem ipsum dolor sit amet, cons ectetuer adipiscing elit, sed diam nonummy nibh euismod tincidunt ut laoreet dolore magna aliquam erat volutpat. Ut wisi enim ad minim veniam, quis nostrud exerci tation ullamcorper suscipit lobortis nisl ut aliquip ex ea commodo consequat.<br>Lorem ipsum dolor sit amet, consectetuer adipiscing elit, sed diam nonummy nibh euismod tincidunt ut laoreet dolore magna aliquam erat volutpat. Ut wisi enim ad minim veniam, quis nostrud exerci tation ullamcorper suscipit lobortis nisl ut aliquip ex ea com</p>

  <div class="abs brand brand--back"><span class="brand-mark"></span><div class="brand-name">KVR<span>Medical Services</span></div></div>
</section>

</body>
</html>
```